Business Card Design Project

Financial planning, Insurance and Real estate - Financial Services company

Contact Information for Business Card

Looking for something simple in design -
Tolverin Equity LLC
Tolverin Wealth Managment

```html
<!DOCTYPE html>
<html lang="en">
<head>
<meta charset="utf-8">
<title>Tolverin Wealth Managment – Business Card</title>
<link rel="stylesheet" href="https://fonts.googleapis.com/css2?family=Roboto:wght@400;500&family=Roboto+Condensed:wght@400;700&display=swap">
<style>
  :root {
    --page-bg: #e9e9e7;
    --card-bg: #fbfbfb;
    --brand-blue: #1a86c8;
    --text-grey: #5e5e5e;
    --rule-grey: #c9c9c9;
    --card-shadow: rgba(0, 0, 0, 0.18);
  }
  html, body {
    margin: 0;
    padding: 0;
    width: 1200px;
    height: 950px;
    overflow: hidden;
    background: var(--page-bg);
  }
  .canvas {
    width: 1200px;
    height: 950px;
    display: flex;
    align-items: center;
    justify-content: center;
  }
  .card {
    position: relative;
    width: 1050px;
    height: 600px;
    background: var(--card-bg);
    box-shadow: 0 10px 30px var(--card-shadow);
    display: flex;
    overflow: hidden;
  }
  .card-brand {
    width: 500px;
    display: flex;
    flex-direction: column;
    align-items: center;
    justify-content: center;
    gap: 34px;
  }
  .brand-mark {
    width: 150px;
    height: 150px;
  }
  .brand-name {
    font-family: "Roboto Condensed", sans-serif;
    font-weight: 700;
    font-size: 34px;
    color: var(--brand-blue);
    margin: 0;
    letter-spacing: 0.2px;
  }
  .card-divider {
    width: 2px;
    margin: 70px 0;
    background: linear-gradient(to bottom, transparent, var(--rule-grey) 30%, var(--rule-grey) 70%, transparent);
  }
  .card-contact {
    flex: 1;
    padding: 78px 0 0 62px;
    font-family: "Roboto", sans-serif;
    color: var(--text-grey);
  }
  .person-name {
    font-family: "Roboto Condensed", sans-serif;
    font-weight: 400;
    font-size: 40px;
    line-height: 1;
    color: var(--brand-blue);
    margin: 0;
    text-transform: uppercase;
  }
  .person-title {
    font-family: "Roboto Condensed", sans-serif;
    font-size: 30px;
    line-height: 1.2;
    margin: 4px 0 22px;
    text-transform: uppercase;
  }
  .contact-block {
    margin: 0 0 20px;
    font-size: 27px;
    line-height: 1.3;
    font-style: normal;
  }
  .contact-label {
    display: inline-block;
    min-width: 44px;
  }
</style>
</head>
<body>
<div class="canvas">
  <article class="card">
    <section class="card-brand">
      <svg class="brand-mark" viewBox="0 0 150 150" aria-hidden="true">
        <circle cx="75" cy="75" r="62" fill="none" stroke="var(--brand-blue)" stroke-width="10"/>
      </svg>
      <h1 class="brand-name">Tolverin Wealth Managment</h1>
    </section>
    <div class="card-divider"></div>
    <section class="card-contact">
      <h2 class="person-name">Alan Marsh</h2>
      <p class="person-title">CEO/Founder</p>
      <address class="contact-block">
        Tolverin Equity LLC<br>
        4120 Harbor View Road<br>
        Juneau, Alaska 99801
      </address>
      <p class="contact-block">
        <span class="contact-label">(P)</span> 907 555 0142<br>
        <span class="contact-label">(M)</span> 907 555 0187<br>
        <span class="contact-label">(F)</span> 907 555 0163<br>
        alan@tolverin.com<br>
        www.tolverin.com
      </p>
    </section>
  </article>
</div>
</body>
</html>
```